Quarrow financial services, is a financial company that provides consultancy, brokerage services, and funding.

we will be providing the clients with insights, knowledge and data with regards to the financial markets.

with the brokerage services we will try to find the suitable counterparts that provide them with the best investments that suits their needs and expected return.

Target Market(s)

financial institutions, Corporates, high-net worth individuals

Industry/Entity Type

Financial Service

Contact Information for Business Card

Font styles to use
Other font styles liked:
• applemyungjo

Colors
00a990
848484

Requirements
Must have
• the logo at the back
Nice to have
• Finesse
Should not have
• boldness

```html
<!DOCTYPE html>
<html lang="en">
<head>
<meta charset="utf-8">
<title>Quarrow Financial Services – Business Card</title>
<link rel="stylesheet" href="https://fonts.googleapis.com/css2?family=Montserrat:wght@400;600&display=swap">
<style>
  :root {
    --slate: #3e484e;
    --leaf: #7cb236;
    --paper: #ffffff;
    --ink: #3b4145;
    --stage: #2a2a2a;
  }
  * { box-sizing: border-box; margin: 0; padding: 0; }
  html, body { width: 1200px; height: 900px; overflow: hidden; }
  body {
    background: var(--stage);
    position: relative;
    font-family: "Montserrat", sans-serif;
  }
  .card {
    position: absolute;
    left: 320px;
    width: 560px;
    height: 320px;
    overflow: hidden;
    box-shadow: 0 10px 30px rgba(0,0,0,.45);
  }
  .card--front { top: 100px; background: var(--slate); }
  .card--back  { top: 480px; background: var(--slate); }

  /* front */
  .front__name {
    position: absolute;
    left: 0; right: 0; top: 120px;
    text-align: center;
    color: var(--paper);
    font-size: 30px;
    font-weight: 400;
    letter-spacing: 3px;
    line-height: 1.3;
  }
  .front__url {
    position: absolute;
    right: 40px; bottom: 40px;
    color: var(--paper);
    font-size: 15px;
  }
  .accent { color: var(--leaf); }

  /* back */
  .back__brand {
    position: absolute;
    left: 0; top: 0;
    width: 250px; height: 320px;
    background: var(--paper);
    border-right: 3px solid var(--leaf);
    display: flex;
    align-items: center;
    justify-content: center;
  }
  .brand-name {
    width: 200px;
    text-align: center;
    color: var(--ink);
    font-size: 20px;
    font-weight: 400;
    letter-spacing: 2px;
    line-height: 1.35;
  }
  .brand-notch { position: absolute; left: 252px; top: 62px; }

  .contact {
    position: absolute;
    left: 290px; top: 62px;
    color: var(--paper);
  }
  .contact__name { color: var(--leaf); font-size: 20px; font-weight: 600; }
  .contact__role { font-size: 13px; margin-top: 2px; }
  .contact__address { font-size: 13px; line-height: 1.35; margin: 14px 0 0 18px; }
  .contact__list { list-style: none; margin: 6px 0 0 36px; font-size: 13px; line-height: 1.4; }
  .contact__list li { display: flex; align-items: center; gap: 8px; }
  .contact__list svg { width: 10px; height: 10px; flex: none; }
</style>
</head>
<body>

<section class="card card--front">
  <div class="front__name">QUARROW<br>FINANCIAL SERVICES</div>
  <div class="front__url">www.<span class="accent">quarrowfinancial</span>.com</div>
</section>

<section class="card card--back">
  <div class="back__brand">
    <div class="brand-name">QUARROW<br>FINANCIAL SERVICES</div>
  </div>
  <svg class="brand-notch" width="18" height="28" viewBox="0 0 18 28" aria-hidden="true">
    <polygon points="0,0 18,14 0,28" fill="#ffffff"/>
  </svg>

  <div class="contact">
    <div class="contact__name">Maren Ellis</div>
    <div class="contact__role">Director</div>
    <div class="contact__address">P.O. Box 3318<br>Lakeport, MI 49602</div>
    <ul class="contact__list">
      <li>
        <svg viewBox="0 0 10 10"><path d="M2 1 L4 1 L4.6 3 L3.4 3.8 Q4.4 5.8 6.2 6.6 L7 5.4 L9 6 L9 8 Q5 9.4 1 3 Z" fill="#7cb236"/></svg>
        <span>(555) 214-3390</span>
      </li>
      <li>
        <svg viewBox="0 0 10 10"><rect x="2.5" y="0.5" width="5" height="9" rx="1" fill="none" stroke="#7cb236" stroke-width="1.2"/></svg>
        <span>(555) 214-7712</span>
      </li>
      <li>
        <svg viewBox="0 0 10 10"><rect x="0.5" y="2" width="9" height="6" fill="none" stroke="#7cb236" stroke-width="1.1"/><path d="M0.5 2 L5 5.5 L9.5 2" fill="none" stroke="#7cb236" stroke-width="1.1"/></svg>
        <span>info@quarrowfinancial.com</span>
      </li>
      <li>
        <svg viewBox="0 0 10 10"><circle cx="5" cy="5" r="4.4" fill="#7cb236"/></svg>
        <span>www.<span class="accent">quarrowfinancial</span>.com</span>
      </li>
    </ul>
  </div>
</section>

</body>
</html>
```